Computer Service Provider in Need of New Letterhead Design

We are Larkvale Computer Services, a computer/IT services company that provides IT Support, software, hardware, virus monitoring, etc. in Vermont. We are looking for new letterhead, that is both professional and matches the current theme of our business cards & website.
Please note that we want to include the following information:
www.Larkvale.example
802-555-0147
47 Fernwick Hollow Road, Brackenford, VT 05990
Responsive Support • Friendly Experts • Reliable Results
I will be attaching our logo along with the business card images.
We would love to have the

```html
<!DOCTYPE html>
<html lang="en">
<head>
<meta charset="utf-8">
<title>Larkvale Computer Services – Letterhead</title>
<link rel="stylesheet" href="https://fonts.googleapis.com/css2?family=Source+Sans+3:wght@400;600;700&display=swap">
<style>
  :root {
    --brand-blue: #2a5d8f;
    --brand-navy: #1f4a78;
    --brand-orange: #f2a23a;
    --ink: #3c4650;
    --paper: #ffffff;
    --backdrop: #dfe6ee;
  }
  * { box-sizing: border-box; margin: 0; padding: 0; }
  html, body {
    width: 1200px; height: 784px; overflow: hidden;
    background: var(--backdrop);
    font-family: "Source Sans 3", "Helvetica Neue", Arial, sans-serif;
  }
  .letterhead {
    position: absolute; left: 314px; top: 22px;
    width: 572px; height: 740px;
    background: var(--paper);
    box-shadow: 0 2px 10px rgba(30, 60, 100, 0.18);
    overflow: hidden;
  }
  .corner-bars { position: absolute; }
  .corner-bars--top-left { left: 0; top: 0; }
  .corner-bars--top-right { right: 0; top: 0; }

  .brand {
    position: absolute; left: 40px; top: 26px;
    display: flex; align-items: center; gap: 8px;
    color: var(--brand-navy);
  }
  .brand__square { width: 26px; height: 26px; background: var(--brand-navy); }
  .brand__name { font-size: 17px; font-weight: 700; letter-spacing: 0.2px; }

  .tagline {
    position: absolute; right: 30px; top: 30px;
    list-style: none; text-align: left;
    font-size: 8.5px; font-weight: 400; letter-spacing: 0.6px; text-transform: uppercase;
    color: var(--brand-orange); line-height: 1.45;
  }
  .tagline li::before {
    content: ""; display: inline-block; width: 3.5px; height: 3.5px;
    border-radius: 50%; background: var(--brand-navy);
    margin-right: 5px; vertical-align: middle;
  }

  .contact {
    position: absolute; left: 28px; bottom: 30px;
    display: flex; align-items: center; gap: 14px;
    font-size: 9px; font-style: normal; color: var(--ink);
  }
  .contact__item { display: flex; align-items: center; gap: 4px; white-space: nowrap; }
  .contact__icon { width: 9px; height: 9px; flex: none; }

  .footer-bands { position: absolute; left: 0; bottom: 0; }
  .website {
    position: absolute; right: 14px; bottom: 8px;
    font-size: 11px; font-weight: 700; color: #fff; letter-spacing: 0.2px;
  }
</style>
</head>
<body>
  <main class="letterhead">
    <svg class="corner-bars corner-bars--top-left" width="60" height="14" viewBox="0 0 60 14" aria-hidden="true">
      <rect x="22" y="0" width="38" height="4" fill="var(--brand-blue)"/>
      <rect x="0" y="6" width="30" height="4" fill="var(--brand-orange)"/>
    </svg>
    <svg class="corner-bars corner-bars--top-right" width="50" height="14" viewBox="0 0 50 14" aria-hidden="true">
      <rect x="20" y="0" width="30" height="4" fill="var(--brand-blue)"/>
      <rect x="0" y="6" width="28" height="4" fill="var(--brand-orange)"/>
    </svg>

    <header class="brand">
      <span class="brand__square"></span>
      <span class="brand__name">Larkvale Computer Services</span>
    </header>

    <ul class="tagline">
      <li>Responsive Support</li>
      <li>Friendly Experts</li>
      <li>Reliable Results</li>
    </ul>

    <address class="contact">
      <span class="contact__item">
        <svg class="contact__icon" viewBox="0 0 10 10" aria-hidden="true"><circle cx="5" cy="5" r="5" fill="var(--brand-orange)"/><path d="M5 2.2a1.8 1.8 0 0 0-1.8 1.8C3.2 5.4 5 7.8 5 7.8S6.8 5.4 6.8 4A1.8 1.8 0 0 0 5 2.2z" fill="#fff"/></svg>
        47 Fernwick Hollow Road, Brackenford, VT 05990
      </span>
      <span class="contact__item">
        <svg class="contact__icon" viewBox="0 0 10 10" aria-hidden="true"><circle cx="5" cy="5" r="5" fill="var(--brand-orange)"/><path d="M3.3 2.5l1 .1.4 1.2-.6.5a3.5 3.5 0 0 0 1.6 1.6l.5-.6 1.2.4.1 1-.8.6C4.8 7.2 2.8 5.2 2.7 3.3z" fill="#fff"/></svg>
        802-555-0147
      </span>
      <span class="contact__item">
        <svg class="contact__icon" viewBox="0 0 10 10" aria-hidden="true"><circle cx="5" cy="5" r="5" fill="var(--brand-orange)"/><rect x="2.6" y="3.2" width="4.8" height="3.6" fill="#fff"/><path d="M2.6 3.2L5 5.2l2.4-2" stroke="var(--brand-orange)" stroke-width="0.6" fill="none"/></svg>
        office@larkvale.example
      </span>
    </address>

    <svg class="footer-bands" width="572" height="26" viewBox="0 0 572 26" aria-hidden="true">
      <polygon points="0,8 190,8 186,12 0,12" fill="var(--brand-orange)"/>
      <polygon points="196,8 300,8 296,12 192,12" fill="var(--brand-blue)"/>
      <polygon points="306,8 410,8 406,12 302,12" fill="var(--brand-orange)"/>
      <rect x="0" y="15" width="572" height="5" fill="var(--brand-blue)"/>
      <polygon points="416,0 572,0 572,26 0,26 0,20 410,20" fill="var(--brand-blue)"/>
    </svg>
    <span class="website">www.Larkvale.example</span>
  </main>
</body>
</html>
```